Web Design

Looking for web designer for total service. We would like to make it in English and Japanese for now. Also need to make Tablet version. Our website is www.brookmeridian.com and www.tundravolley .com

```html
<!DOCTYPE html>
<html lang="en">
<head>
<meta charset="utf-8">
<title>Brook Meridian – All Products</title>
<link rel="stylesheet" href="https://fonts.googleapis.com/css2?family=Montserrat:wght@300;400;500;600&family=Dancing+Script:wght@500&display=swap">
<style>
  :root {
    --green: #8fbf3a;
    --green-dark: #7aa82c;
    --text: #6b6b6b;
    --text-dark: #333;
    --muted: #9a9a9a;
    --card-panel: #f4f4f4;
    --band: #f0f0f0;
    --footer: #5f6673;
    --white: #ffffff;
    --lemon: #f7d417;
    --berry: #d8323a;
  }
  * { box-sizing: border-box; margin: 0; padding: 0; }
  html, body { width: 1200px; height: 2620px; overflow: hidden; }
  body { position: relative; background: var(--white); font-family: "Montserrat", sans-serif; color: var(--text); }
  .abs { position: absolute; }

  /* header */
  .site-header { position: absolute; left: 0; top: 0; width: 1200px; height: 61px; background: var(--white); box-shadow: 0 2px 6px rgba(0,0,0,.06); z-index: 3; }
  .nav-link { position: absolute; top: 24px; font-size: 13px; color: var(--muted); transform: translateX(-50%); white-space: nowrap; }
  .nav-link.is-active::before { content: ""; position: absolute; left: 50%; top: -24px; width: 68px; height: 4px; margin-left: -34px; background: var(--green); }
  .cart-link { position: absolute; left: 940px; top: 20px; font-size: 13px; color: var(--text-dark); }
  .cart-count { position: absolute; left: 990px; top: 36px; font-size: 9px; color: var(--green); }
  .header-logo { position: absolute; left: 541px; top: 0; width: 114px; height: 91px; background: var(--white); box-shadow: 0 2px 6px rgba(0,0,0,.12); z-index: 4; display: flex; flex-direction: column; align-items: center; justify-content: center; gap: 6px; }
  .logo-mark { width: 18px; height: 18px; background: var(--green); }
  .logo-name { font-size: 12px; font-weight: 500; color: var(--green); letter-spacing: 1px; text-align: center; line-height: 1.2; }

  /* decorations */
  .fruit { position: absolute; z-index: 2; }
  .fruit.lemon { background: var(--lemon); border-radius: 50%; }
  .fruit.berry { background: var(--berry); border-radius: 45% 45% 50% 50% / 40% 40% 60% 60%; }

  /* products heading */
  .page-title { position: absolute; left: 119px; top: 162px; font-family: "Dancing Script", cursive; font-size: 44px; font-weight: 500; color: var(--text-dark); }
  .filter { position: absolute; top: 182px; width: 184px; height: 33px; border: 1px solid var(--green); font-size: 12px; color: var(--green); padding: 8px 10px; }
  .filter::after { content: ""; position: absolute; right: 14px; top: 14px; border: 5px solid transparent; border-top: 6px solid var(--green); }

  /* product cards */
  .product-card { position: absolute; width: 272px; height: 252px; background: var(--white); box-shadow: 0 2px 10px rgba(0,0,0,.14); }
  .product-card .panel { position: absolute; inset: 8px; background: var(--card-panel); }
  .product-shot { position: absolute; top: -125px; left: 50%; transform: translateX(-50%); height: 192px; background: linear-gradient(90deg, #c6d67a, #e9a8bf 50%, #c9a877); border-radius: 2px; box-shadow: 0 3px 6px rgba(0,0,0,.2); z-index: 1; }
  .product-shot.single { width: 84px; background: linear-gradient(180deg, #d2b48a, #b8d06a 45%, #cda878); }
  .product-shot.triple { width: 196px; }
  .product-shot.double { width: 136px; left: 52%; }
  .price { position: absolute; top: 98px; width: 100%; text-align: center; font-size: 22px; color: var(--green); }
  .blurb { position: absolute; top: 133px; width: 100%; text-align: center; font-size: 17px; line-height: 23px; color: var(--text); font-weight: 300; }
  .buy-btn { position: absolute; top: 194px; left: 50%; transform: translateX(-50%); width: 131px; height: 33px; border: 1px solid #9aa0aa; border-radius: 17px; font-size: 10px; font-weight: 600; color: #7a8090; text-align: center; line-height: 31px; background: transparent; }

  /* pagination */
  .pagination { position: absolute; left: 528px; top: 1569px; display: flex; gap: 5px; }
  .page { width: 24px; height: 30px; border: 1px solid #c9dca0; color: var(--green); font-size: 15px; text-align: center; line-height: 28px; }
  .page.is-current { background: var(--green); color: var(--white); font-weight: 600; }

  /* newsletter */
  .newsletter { position: absolute; left: 0; top: 1686px; width: 1200px; height: 361px; background: var(--band); box-shadow: inset 0 3px 5px rgba(0,0,0,.05); }
  .newsletter h2 { position: absolute; top: 92px; width: 100%; text-align: center; font-size: 30px; font-weight: 300; color: #4a4a4a; }
  .newsletter p { position: absolute; top: 140px; width: 100%; text-align: center; font-size: 16px; line-height: 23px; color: var(--muted); font-weight: 300; }
  .email-field { position: absolute; left: 323px; top: 213px; width: 543px; height: 61px; background: var(--white); border-radius: 31px; box-shadow: 0 2px 8px rgba(0,0,0,.08); font-size: 16px; color: #aaa; padding: 20px 33px; font-weight: 300; }
  .email-field svg { position: absolute; right: 30px; top: 21px; }
  .newsletter-pack { position: absolute; left: 52px; top: 218px; width: 172px; height: 166px; background: linear-gradient(90deg, #c6d67a, #e9a8bf 50%, #c9a877); z-index: 2; }

  /* footer */
  .site-footer { position: absolute; left: 0; top: 2047px; width: 1200px; height: 573px; background: linear-gradient(160deg, #6a717d, var(--footer) 50%, #555c68); color: var(--white); }
  .site-footer h2 { position: absolute; top: 62px; width: 100%; text-align: center; font-family: "Dancing Script", cursive; font-size: 46px; font-weight: 500; }
  .field { position: absolute; font-size: 14px; border-bottom: 1px solid rgba(255,255,255,.5); padding-bottom: 8px; }
  .captcha { position: absolute; left: 245px; top: 284px; display: flex; align-items: center; gap: 8px; font-size: 10px; }
  .captcha i { width: 16px; height: 16px; background: var(--white); display: block; }
  .reply-note { position: absolute; left: 700px; top: 286px; width: 104px; text-align: right; font-size: 10px; line-height: 13px; }
  .send-btn { position: absolute; left: 816px; top: 285px; width: 147px; height: 35px; background: var(--green); font-size: 12px; font-weight: 600; text-align: center; line-height: 35px; }
  .footer-rule { position: absolute; left: 148px; top: 396px; width: 904px; height: 1px; background: rgba(255,255,255,.2); }
  .footer-logo { position: absolute; left: 140px; top: 422px; width: 126px; display: flex; flex-direction: column; align-items: center; gap: 8px; }
  .footer-logo .logo-mark { background: var(--white); width: 24px; height: 24px; }
  .footer-logo .logo-name { color: var(--white); font-size: 14px; }
  .footer-col { position: absolute; top: 421px; font-size: 11px; line-height: 18px; }
  .footer-col h3 { font-size: 12px; font-weight: 600; margin-bottom: 5px; }
  .footer-col li { list-style: none; color: rgba(255,255,255,.9); }
</style>
</head>
<body>

<header class="site-header">
  <span class="nav-link" style="left:219px">About us</span>
  <span class="nav-link is-active" style="left:323px">Contact us</span>
  <span class="nav-link" style="left:442px">Our Products</span>
  <span class="nav-link" style="left:775px">Online Shopping</span>
  <span class="nav-link" style="left:882px">Login</span>
  <span class="cart-link">Shopping cart</span>
  <span class="cart-count">0 items</span>
</header>
<div class="header-logo">
  <span class="logo-mark"></span>
  <span class="logo-name">BROOK<br>MERIDIAN</span>
</div>

<div class="fruit lemon" role="img" aria-label="Lemon" style="left:-40px;top:40px;width:120px;height:92px;"></div>
<div class="fruit berry" role="img" aria-label="Strawberry" style="left:58px;top:256px;width:40px;height:46px;"></div>
<div class="fruit lemon" role="img" aria-label="Lemon" style="left:1065px;top:283px;width:98px;height:74px;"></div>
<div class="fruit lemon" role="img" aria-label="Lemon" style="left:88px;top:615px;width:96px;height:72px;"></div>
<div class="fruit berry" role="img" aria-label="Strawberry" style="left:1108px;top:742px;width:40px;height:46px;"></div>
<div class="fruit berry" role="img" aria-label="Strawberry" style="left:97px;top:1496px;width:40px;height:46px;"></div>
<div class="fruit lemon" role="img" aria-label="Lemon" style="left:1050px;top:1458px;width:96px;height:74px;"></div>

<h1 class="page-title">All Products</h1>
<div class="filter" style="left:510px">Category 1</div>
<div class="filter" style="left:702px">Category 2</div>
<div class="filter" style="left:894px">Category 3</div>

<main class="product-grid">
  <!-- row 1 -->
  <article class="product-card" style="left:126px;top:405px"><div class="panel"></div><div class="product-shot single" role="img" aria-label="Pancake mix bag"></div><div class="price">$7,99</div><div class="blurb">Your choice what text<br>to write here</div><div class="buy-btn">BUY NOW</div></article>
  <article class="product-card" style="left:472px;top:405px"><div class="panel"></div><div class="product-shot triple" role="img" aria-label="Three pancake mix bags"></div><div class="price">$19,99</div><div class="blurb">Your choice what text<br>to write here</div><div class="buy-btn">BUY NOW</div></article>
  <article class="product-card" style="left:805px;top:405px"><div class="panel"></div><div class="product-shot double" role="img" aria-label="Two pancake mix bags"></div><div class="price">$12,99</div><div class="blurb">Your choice what text<br>to write here</div><div class="buy-btn">BUY NOW</div></article>
  <!-- row 2 -->
  <article class="product-card" style="left:126px;top:832px"><div class="panel"></div><div class="product-shot single" role="img" aria-label="Pancake mix bag"></div><div class="price">$7,99</div><div class="blurb">Your choice what text<br>to write here</div><div class="buy-btn">BUY NOW</div></article>
  <article class="product-card" style="left:472px;top:832px"><div class="panel"></div><div class="product-shot triple" role="img" aria-label="Three pancake mix bags"></div><div class="price">$19,99</div><div class="blurb">Your choice what text<br>to write here</div><div class="buy-btn">BUY NOW</div></article>
  <article class="product-card" style="left:805px;top:832px"><div class="panel"></div><div class="product-shot double" role="img" aria-label="Two pancake mix bags"></div><div class="price">$12,99</div><div class="blurb">Your choice what text<br>to write here</div><div class="buy-btn">BUY NOW</div></article>
  <!-- row 3 -->
  <article class="product-card" style="left:126px;top:1258px"><div class="panel"></div><div class="product-shot single" role="img" aria-label="Pancake mix bag"></div><div class="price">$7,99</div><div class="blurb">Your choice what text<br>to write here</div><div class="buy-btn">BUY NOW</div></article>
  <article class="product-card" style="left:472px;top:1258px"><div class="panel"></div><div class="product-shot triple" role="img" aria-label="Three pancake mix bags"></div><div class="price">$19,99</div><div class="blurb">Your choice what text<br>to write here</div><div class="buy-btn">BUY NOW</div></article>
  <article class="product-card" style="left:805px;top:1258px"><div class="panel"></div><div class="product-shot double" role="img" aria-label="Two pancake mix bags"></div><div class="price">$12,99</div><div class="blurb">Your choice what text<br>to write here</div><div class="buy-btn">BUY NOW</div></article>
</main>

<nav class="pagination">
  <span class="page">1</span><span class="page">2</span><span class="page is-current">3</span><span class="page">4</span><span class="page">5</span>
</nav>

<section class="newsletter">
  <h2>Subscribe to our newsletter</h2>
  <p>Lorem ipsum dolor sit amet, consec<br>scing elit commodo ligula.</p>
  <div class="email-field">Your email address here...
    <svg width="28" height="20" viewBox="0 0 28 20"><rect x="1" y="1" width="26" height="18" fill="none" stroke="#8fbf3a" stroke-width="2"/><path d="M1 1 L14 11 L27 1" fill="none" stroke="#8fbf3a" stroke-width="2"/></svg>
  </div>
  <div class="newsletter-pack" role="img" aria-label="Three pancake mix bags"></div>
</section>

<footer class="site-footer" role="img" aria-label="Blurred photo of pancake mix packaging behind the contact area">
  <h2>Get in touch</h2>
  <div class="field" style="left:245px;top:164px;width:344px">Your Full Name...</div>
  <div class="field" style="left:615px;top:164px;width:342px">Your Email Address...</div>
  <div class="field" style="left:245px;top:227px;width:712px">Write a message for us...</div>
  <div class="captcha"><i></i>I'm not a robot</div>
  <div class="reply-note">We will answer<br>in 24hours</div>
  <div class="send-btn">SEND A MESSSAGE</div>
  <div class="footer-rule"></div>
  <div class="footer-logo"><span class="logo-mark"></span><span class="logo-name">BROOK<br>MERIDIAN</span></div>
  <div class="footer-col" style="left:383px"><h3>Navigation</h3><ul><li>How it Works</li><li>Pricing Page</li><li>Try Our Tools</li><li>Sign Up</li><li>Login</li></ul></div>
  <div class="footer-col" style="left:552px"><h3>Policy</h3><ul><li>Conditions &amp; Terms</li><li>About us</li><li>Privacy Policy</li><li>Write to us</li><li>Block Security</li></ul></div>
  <div class="footer-col" style="left:742px"><h3>Contacts</h3><ul><li>Your Street Adress</li><li>Phone Numbers</li><li>Email Addresses</li><li>Working Hours</li><li>Products</li></ul></div>
  <div class="footer-col" style="left:926px"><h3>Social</h3><ul><li>Friendwall</li><li>Circleplus</li><li>Chirpline</li></ul></div>
</footer>

</body>
</html>
```